Medical Device Company needs website

We are a start-up medical device company looking to sell boot (foot) and brace (ankle) products on Shopify. We are still working on the name but you can use Tavrix as a placeholder- no logo yet)

Website information:
- Look: modern/tech with clean lines and symmetry.
- Colors: teal, white, black, and greys.
- Headers: home, shop, about us, help, blog
- Icons (upper right): search, my account and shopping cart
-place to sign up for newsletter

```html
<!DOCTYPE html>
<html lang="en">
<head>
<meta charset="utf-8">
<title>Tavrix Medical Device</title>
<link rel="stylesheet" href="https://fonts.googleapis.com/css2?family=Montserrat:wght@500;600;700;800&family=Open+Sans:wght@400;600;700&display=swap">
<style>
:root{
  --teal:#2e7480;
  --teal-dark:#245f69;
  --ink:#151515;
  --text:#333;
  --grey:#777;
  --line:#e3e3e3;
  --soft:#f4f6f7;
  --white:#fff;
}
*{box-sizing:border-box;margin:0;padding:0}
html,body{width:1200px;height:3096px;overflow:hidden}
body{font-family:"Open Sans",Arial,sans-serif;color:var(--text);background:var(--white);position:relative}
a{color:inherit;text-decoration:none}
h1,h2,h3,.logo,.nav a,.btn{font-family:"Montserrat",Arial,sans-serif}

/* utility bar */
.utility{height:32px;position:relative}
.utility-strip{position:absolute;right:0;top:0;width:400px;height:32px;background:var(--teal);display:flex;align-items:center;justify-content:flex-end;gap:28px;padding-right:60px;color:#fff;font-size:12px;font-weight:600}
.utility-strip span{display:flex;align-items:center;gap:6px}

/* header */
.header{height:80px;display:flex;align-items:center;padding:0 110px}
.logo{font-size:26px;font-weight:800;color:var(--ink);letter-spacing:1px}
.nav{margin-left:auto;display:flex;align-items:center;gap:38px}
.nav a{font-size:14px;font-weight:700;color:var(--ink);position:relative}
.nav a.active{color:var(--teal)}
.nav a.active::after{content:"";position:absolute;left:50%;bottom:-10px;width:6px;height:6px;border-radius:50%;background:var(--teal);transform:translateX(-50%)}
.btn{display:inline-flex;align-items:center;justify-content:center;border-radius:30px;font-weight:700;font-size:14px;letter-spacing:.5px}
.btn-teal{background:var(--teal);color:#fff}
.nav .btn{padding:12px 26px;color:#fff}

/* hero */
.hero{height:560px;position:relative;overflow:hidden}
.hero-photo{position:absolute;inset:0;background:linear-gradient(90deg,#1b1f22 0%,#2f3336 35%,#8a8f93 60%,#d9dcde 85%,#c8ccce 100%)}
.hero-content{position:absolute;left:110px;top:150px;width:520px;color:#fff}
.hero h1{font-size:40px;font-weight:800;line-height:1.15;letter-spacing:.5px}
.hero p{font-size:17px;font-weight:600;line-height:1.45;margin-top:14px}
.hero .btn{margin-top:56px;padding:16px 34px}

/* section title */
.section-title{text-align:center}
.section-title h2{font-size:34px;font-weight:800;color:var(--ink);letter-spacing:1px}
.section-title i{display:block;width:60px;height:3px;background:var(--teal);margin:14px auto 0}

/* featured */
.featured{height:680px;padding-top:80px;position:relative}
.tabs{display:flex;justify-content:center;gap:24px;margin-top:32px}
.tab{display:flex;align-items:center;gap:16px;height:44px;width:160px;border:1px solid #cfd8da;border-radius:30px;font-family:"Montserrat",sans-serif;font-weight:700;font-size:13px;color:var(--ink)}
.tab .dot{width:44px;height:44px;border-radius:50%;background:var(--soft);border:1px solid #cfd8da;margin-left:-1px;display:flex;align-items:center;justify-content:center}
.tab.on{background:var(--teal);color:#fff;border-color:var(--teal)}
.tab.on .dot{background:#fff;border-color:var(--teal)}
.products{display:flex;justify-content:center;gap:24px;margin-top:40px;position:relative}
.card{width:222px;height:364px;background:#fff;border:1px solid var(--line);display:flex;flex-direction:column;align-items:center;padding:20px 16px;position:relative}
.card.hot{border:2px solid var(--teal);box-shadow:0 10px 26px rgba(0,0,0,.15);transform:translateY(-14px)}
.heart{position:absolute;right:10px;top:10px;width:28px;height:28px;border-radius:50%;background:var(--teal);display:flex;align-items:center;justify-content:center}
.card-img{width:170px;height:170px;background:radial-gradient(circle,#5a5e62 0%,#2a2c2e 55%,#fff 72%)}
.card h3{font-family:"Open Sans",sans-serif;font-size:14px;font-weight:700;color:var(--ink);text-align:center;line-height:1.35;margin-top:18px;height:40px}
.price{font-size:15px;font-weight:600;color:var(--ink);margin-top:10px}
.choose{margin-top:auto;width:170px;height:34px;background:var(--ink);color:#fff;font-size:12px;font-weight:700;display:flex;align-items:center;justify-content:center;clip-path:polygon(0 0,100% 0,92% 100%,0 100%);font-family:"Montserrat",sans-serif}
.card.hot .choose{background:var(--teal)}
.arrow{position:absolute;top:170px}
.arrow.left{left:40px}.arrow.right{right:40px}

/* about */
.about{height:536px;background:var(--teal);position:relative;color:#fff}
.collage{position:absolute;left:110px;top:64px;width:470px;height:410px}
.collage .frame{position:absolute;border:3px solid #fff}
.collage .ph{position:absolute}
.about-text{position:absolute;left:670px;top:100px;width:420px}
.about h2{font-size:34px;font-weight:800;letter-spacing:1px}
.about h2+i{display:block;width:60px;height:3px;background:#fff;margin:12px 0 22px}
.about p{font-size:13px;line-height:1.6;margin-bottom:14px}
.about .btn{background:#fff;color:var(--teal);padding:15px 34px;margin-top:18px}

/* blog */
.blog{height:624px;padding-top:84px}
.posts{display:flex;justify-content:center;gap:40px;margin-top:40px}
.post{width:300px;height:386px;background:#fff;box-shadow:0 6px 22px rgba(0,0,0,.13);border-radius:6px;overflow:hidden;text-align:center}
.post-img{height:206px;margin:14px 14px 0;border-radius:4px}
.post .date{display:flex;justify-content:center;align-items:center;gap:8px;color:var(--teal);font-size:12px;font-weight:600;margin-top:18px}
.post h3{font-family:"Open Sans",sans-serif;font-size:15px;font-weight:700;color:var(--ink);margin-top:8px}
.post p{font-size:12px;color:var(--grey);line-height:1.5;margin:8px 26px 0}
.post .more{display:inline-flex;align-items:center;gap:8px;color:var(--teal);font-weight:700;font-size:13px;margin-top:12px;font-family:"Montserrat",sans-serif}

/* newsletter */
.newsletter{height:120px;background:var(--ink);display:flex;align-items:center;padding:0 110px;color:#fff;margin-top:40px}
.nl-head{display:flex;align-items:center;gap:22px}
.nl-head h2{font-size:40px;font-weight:700;letter-spacing:1px;line-height:1}
.nl-head p{font-size:13px;margin-top:6px}
.nl-form{margin-left:auto;display:flex;width:440px;height:52px}
.nl-form .field{flex:1;border:1px solid #fff;border-right:none;display:flex;align-items:center;gap:12px;padding-left:16px;color:#ccc;font-size:14px}
.nl-form .send{width:60px;background:#fff;display:flex;align-items:center;justify-content:center}

/* footer */
.footer{height:336px;position:relative;padding:48px 110px 0;display:flex}
.brand{width:360px;padding-top:66px}
.brand .logo{font-size:30px}
.socials{display:flex;gap:10px;margin-top:16px}
.socials span{width:30px;height:30px;border:1px solid var(--ink);border-radius:50%}
.col{width:230px}
.col h3{font-size:15px;font-weight:700;color:var(--ink);margin-bottom:16px}
.col li{list-style:none;font-size:13px;color:var(--text);margin-bottom:9px}
.contact{width:260px}
.contact .row{display:flex;gap:10px;margin-bottom:14px}
.contact b{display:block;font-size:13px;color:var(--ink)}
.contact small{font-size:12px;color:var(--grey);line-height:1.5}
.top-btn{position:absolute;right:50px;bottom:20px;width:38px;height:38px;border-radius:50%;background:var(--teal);display:flex;align-items:center;justify-content:center}
.copyright{position:absolute;left:0;right:0;bottom:0;height:48px;border-top:1px solid var(--line);display:flex;align-items:center;justify-content:center;font-size:13px;color:var(--grey)}
</style>
</head>
<body>

<div class="utility">
  <div class="utility-strip">
    <span><svg width="12" height="12" viewBox="0 0 12 12"><circle cx="5" cy="5" r="3.6" fill="none" stroke="#fff" stroke-width="1.6"/><path d="M8 8l3 3" stroke="#fff" stroke-width="1.6"/></svg>Search</span>
    <span><svg width="12" height="12" viewBox="0 0 12 12"><circle cx="6" cy="3.5" r="2.6" fill="#fff"/><path d="M1 12c0-3 2.2-5 5-5s5 2 5 5z" fill="#fff"/></svg>My Account</span>
    <span><svg width="14" height="12" viewBox="0 0 14 12"><path d="M0 1h2.5l1.8 7h7.2l1.5-5H4" fill="none" stroke="#fff" stroke-width="1.5"/><circle cx="5" cy="10.5" r="1.2" fill="#fff"/><circle cx="10.5" cy="10.5" r="1.2" fill="#fff"/></svg>Cart</span>
  </div>
</div>

<header class="header">
  <a class="logo" href="#">TAVRIX</a>
  <nav class="nav">
    <a class="active" href="#">HOME</a>
    <a href="#">SHOP</a>
    <a href="#">ABOUT US</a>
    <a href="#">HELP</a>
    <a href="#">BLOG</a>
    <a class="btn btn-teal" href="#">SHOP NOW</a>
  </nav>
</header>

<section class="hero">
  <div class="hero-photo" role="img" aria-label="Clinician in a white coat fitting a walking boot on a seated patient's leg"></div>
  <div class="hero-content">
    <h1>TAVRIX MEDICAL<br>DEVICE</h1>
    <p>Lorem ipsum dolor sit amet, consectetur adipiscing elit, incididunt labore dolore magna aliqua.</p>
    <a class="btn btn-teal" href="#">SHOP NOW</a>
  </div>
</section>

<section class="featured">
  <div class="section-title"><h2>FEATURED PRODUCTS</h2><i></i></div>
  <div class="tabs">
    <div class="tab on"><span class="dot"><svg width="16" height="16" viewBox="0 0 16 16"><path d="M5 1h4v9h5v5H3z" fill="var(--teal)"/></svg></span>ALL</div>
    <div class="tab"><span class="dot"><svg width="16" height="16" viewBox="0 0 16 16"><path d="M5 1h4v9h5v5H3z" fill="#555"/></svg></span>BOOT</div>
    <div class="tab"><span class="dot"><svg width="16" height="16" viewBox="0 0 16 16"><path d="M6 1h4v8l4 3v3H3v-3l3-3z" fill="#555"/></svg></span>ANKLE</div>
  </div>
  <div class="products">
    <article class="card">
      <div class="card-img" role="img" aria-label="Tall grey walking boot"></div>
      <h3>Stride Walking Boot (Tall Non-Pneumatic)</h3>
      <div class="price">$18.90 – $141.73</div>
      <a class="choose" href="#">Choose Options</a>
    </article>
    <article class="card hot">
      <span class="heart"><svg width="14" height="12" viewBox="0 0 14 12"><path d="M7 12L1.2 6.2A3.3 3.3 0 0 1 7 2a3.3 3.3 0 0 1 5.8 4.2z" fill="#fff"/></svg></span>
      <div class="card-img" role="img" aria-label="Black ankle brace shoe"></div>
      <h3>Flexa™ Ankle Brace</h3>
      <div class="price">$18.90 – $141.73</div>
      <a class="choose" href="#">Choose Options</a>
    </article>
    <article class="card">
      <div class="card-img" role="img" aria-label="Black universal knee brace"></div>
      <h3>The Pivot™ Universal KX Knee Brace</h3>
      <div class="price">$18.90 – $141.73</div>
      <a class="choose" href="#">Choose Options</a>
    </article>
    <article class="card">
      <div class="card-img" role="img" aria-label="Hybrid night splint with straps"></div>
      <h3>Hybrid Night Splint</h3>
      <div class="price">$18.90 – $141.73</div>
      <a class="choose" href="#">Choose Options</a>
    </article>
  </div>
  <svg class="arrow left" style="top:420px" width="16" height="28" viewBox="0 0 16 28"><path d="M14 2L3 14l11 12" fill="none" stroke="#222" stroke-width="2.5"/></svg>
  <svg class="arrow right" style="top:420px" width="16" height="28" viewBox="0 0 16 28"><path d="M2 2l11 12L2 26" fill="none" stroke="#222" stroke-width="2.5"/></svg>
</section>

<section class="about">
  <div class="collage">
    <div class="frame" style="left:0;top:0;width:250px;height:200px"></div>
    <div class="ph" role="img" aria-label="Clinician examining a patient's foot" style="left:14px;top:14px;width:230px;height:170px;background:linear-gradient(135deg,#c9ccce,#6b7276)"></div>
    <div class="ph" role="img" aria-label="Patient wearing a walking boot" style="left:0;top:180px;width:300px;height:200px;background:linear-gradient(135deg,#e4e6e8,#3c4e5c)"></div>
    <div class="frame" style="left:230px;top:110px;width:240px;height:300px"></div>
    <div class="ph" role="img" aria-label="Ankle being wrapped with a bandage" style="left:250px;top:130px;width:200px;height:240px;background:linear-gradient(160deg,#b8c3cf,#2e3f63)"></div>
  </div>
  <div class="about-text">
    <h2>ABOUT US</h2><i></i>
    <p>Lorem ipsum dolor sit amet, consectetur adipiscing elit, sed do eiusmod tempor incididunt ut labore et dolore magna aliqua. Ut enim ad minim veniam, quis nostrud exercitation ullamco laboris nisi ut aliquip ex ea commodo consequat.</p>
    <p>Duis aute irure dolor in reprehenderit in voluptate velit esse cillum dolore eu fugiat nulla pariatur. Excepteur sint occaecat cupidatat non proident, sunt in culpa qui officia deserunt mollit anim id est laborum.</p>
    <a class="btn" href="#">LEARN MORE</a>
  </div>
</section>

<section class="blog">
  <div class="section-title"><h2>LATEST BLOG</h2><i></i></div>
  <div class="posts">
    <article class="post">
      <div class="post-img" role="img" aria-label="Hands massaging a foot" style="background:linear-gradient(135deg,#d9b9a3,#7a5540)"></div>
      <div class="date"><svg width="12" height="12" viewBox="0 0 12 12"><rect x="1" y="2" width="10" height="9" fill="none" stroke="var(--teal)" stroke-width="1.4"/><path d="M1 5h10M4 0v3M8 0v3" stroke="var(--teal)" stroke-width="1.4"/></svg>February 2, 2022</div>
      <h3>Lorem ipsum dolor sit amet,</h3>
      <p>Sed ut perspiciatis unde omnis iste natus sit voluptatem accusantium</p>
      <a class="more" href="#">READ MORE <svg width="14" height="14" viewBox="0 0 14 14"><circle cx="7" cy="7" r="7" fill="var(--teal)"/><path d="M4 7h6M7.5 4.5L10 7l-2.5 2.5" fill="none" stroke="#fff" stroke-width="1.4"/></svg></a>
    </article>
    <article class="post">
      <div class="post-img" role="img" aria-label="Ankle wrapped in an elastic bandage" style="background:linear-gradient(135deg,#e8d8c8,#9a7a62)"></div>
      <div class="date"><svg width="12" height="12" viewBox="0 0 12 12"><rect x="1" y="2" width="10" height="9" fill="none" stroke="var(--teal)" stroke-width="1.4"/><path d="M1 5h10M4 0v3M8 0v3" stroke="var(--teal)" stroke-width="1.4"/></svg>February 2, 2022</div>
      <h3>Lorem ipsum dolor sit amet,</h3>
      <p>Sed ut perspiciatis unde omnis iste natus sit voluptatem accusantium</p>
      <a class="more" href="#">READ MORE <svg width="14" height="14" viewBox="0 0 14 14"><circle cx="7" cy="7" r="7" fill="var(--teal)"/><path d="M4 7h6M7.5 4.5L10 7l-2.5 2.5" fill="none" stroke="#fff" stroke-width="1.4"/></svg></a>
    </article>
    <article class="post">
      <div class="post-img" role="img" aria-label="Clinician checking a patient's ankle" style="background:linear-gradient(135deg,#cfd6de,#4a5f7a)"></div>
      <div class="date"><svg width="12" height="12" viewBox="0 0 12 12"><rect x="1" y="2" width="10" height="9" fill="none" stroke="var(--teal)" stroke-width="1.4"/><path d="M1 5h10M4 0v3M8 0v3" stroke="var(--teal)" stroke-width="1.4"/></svg>February 2, 2022</div>
      <h3>Lorem ipsum dolor sit amet,</h3>
      <p>Sed ut perspiciatis unde omnis iste natus sit voluptatem accusantium</p>
      <a class="more" href="#">READ MORE <svg width="14" height="14" viewBox="0 0 14 14"><circle cx="7" cy="7" r="7" fill="var(--teal)"/><path d="M4 7h6M7.5 4.5L10 7l-2.5 2.5" fill="none" stroke="#fff" stroke-width="1.4"/></svg></a>
    </article>
  </div>
</section>

<section class="newsletter">
  <div class="nl-head">
    <svg width="64" height="56" viewBox="0 0 64 56"><path d="M4 22L32 4l28 18v30H4z" fill="none" stroke="#fff" stroke-width="2.5"/><path d="M4 22l28 18 28-18" fill="none" stroke="#fff" stroke-width="2.5"/><rect x="14" y="12" width="36" height="20" fill="none" stroke="#fff" stroke-width="2"/></svg>
    <div><h2>NEWSLETTER</h2><p>Sign up to receive exclusive offers &amp; the best deals</p></div>
  </div>
  <div class="nl-form">
    <div class="field"><svg width="16" height="12" viewBox="0 0 16 12"><rect x="1" y="1" width="14" height="10" fill="none" stroke="#ccc" stroke-width="1.4"/><path d="M1 1l7 6 7-6" fill="none" stroke="#ccc" stroke-width="1.4"/></svg>Email address</div>
    <div class="send"><svg width="22" height="22" viewBox="0 0 22 22"><path d="M1 10L21 1l-7 20-3-8z" fill="#151515"/></svg></div>
  </div>
</section>

<footer class="footer">
  <div class="brand">
    <div class="logo">TAVRIX</div>
    <div class="socials"><span></span><span></span><span></span><span></span></div>
  </div>
  <div class="col">
    <h3>Quick Links</h3>
    <ul><li>Home</li><li>Shop</li><li>About us</li><li>Help</li><li>Blog</li></ul>
  </div>
  <div class="col">
    <h3>About Company</h3>
    <ul><li>Support</li><li>Privacy Policy</li><li>Shipping Policy</li><li>Terms &amp; Conditions</li><li>Sitemap</li></ul>
  </div>
  <div class="col contact">
    <h3>Contact Us</h3>
    <div class="row"><svg width="14" height="14" viewBox="0 0 14 14"><path d="M3 1l2.5 3-1.5 1.5a8 8 0 0 0 4.5 4.5L10 8.5l3 2.5-1.5 2.5C6 13.5.5 8 .5 2.5z" fill="var(--ink)"/></svg><div><b>Phone</b><small>+1 800 555 0142</small></div></div>
    <div class="row"><svg width="14" height="12" viewBox="0 0 14 12"><rect x="0.5" y="1" width="13" height="10" fill="var(--ink)"/><path d="M1 1.5l6 5 6-5" fill="none" stroke="#fff" stroke-width="1.2"/></svg><div><b>Email</b><small>sales@tavrix.com</small></div></div>
    <div class="row"><svg width="12" height="16" viewBox="0 0 12 16"><path d="M6 0a6 6 0 0 1 6 6c0 4-6 10-6 10S0 10 0 6a6 6 0 0 1 6-6z" fill="var(--ink)"/><circle cx="6" cy="6" r="2.2" fill="#fff"/></svg><div><b>Location</b><small>1420 Harbor Ridge Lane, Dover,<br>TN 37058</small></div></div>
  </div>
  <a class="top-btn" href="#"><svg width="14" height="14" viewBox="0 0 14 14"><path d="M2 9l5-5 5 5" fill="none" stroke="#fff" stroke-width="2"/></svg></a>
  <div class="copyright">2024 Copyright - Tavrix | All Right Reserved</div>
</footer>

</body>
</html>
```